Business Card & Full Stationary design For Summit Quarry
Summit Quarry For Marble & Granite
Business Card & Full Stationary design For Summit Quarry  - Construction
Creative Brief
Professional
Eng. Karim Haddouri
C.E.O
14 Shari' Nakhil el Wadi, Rawdatein, Giza, 12487, Egypt
kbh@summitquarry.com.eg
www.summitquarry.com.eg
we need everything to be included in the design ( CD, CD Cover, Letterhead, Envelopes, portfolio cover, etc..)
q7rimo q7rimo
I would highly appreciate if you can provide your concepts showing all the required stationaries including the back side of the B.Card ( Letterhead, 2 size envelope, Portfolio cover, CD, CD cover, Backgrounds for smartphones and Computers .)
Vonto Vonto

```html
<!DOCTYPE html>
<html lang="en">
<head>
<meta charset="utf-8">
<title>Summit Quarry — Business Card</title>
<link rel="stylesheet" href="https://fonts.googleapis.com/css2?family=Montserrat:wght@300;400;600;700&display=swap">
<style>
  :root {
    --backdrop: #4b4845;
    --card: #f7f6f3;
    --gold: #b59c70;
    --ink: #2b2a28;
    --muted: #6d6a65;
  }
  html, body {
    margin: 0;
    width: 1200px;
    height: 896px;
    overflow: hidden;
    background: var(--backdrop);
    font-family: "Montserrat", sans-serif;
  }
  .stage {
    position: relative;
    width: 1200px;
    height: 896px;
  }
  .card {
    position: absolute;
    width: 560px;
    height: 320px;
    background: var(--card);
    border-radius: 26px;
    box-shadow: 0 18px 40px rgba(0,0,0,0.35);
    box-sizing: border-box;
  }
  .card--contact { left: 50px; top: 150px; }
  .card--brand { left: 590px; top: 426px; }

  .contact-list {
    position: absolute;
    top: 48px;
    right: 48px;
    margin: 0;
    padding: 0;
    list-style: none;
  }
  .contact-item {
    display: flex;
    align-items: center;
    gap: 14px;
    margin-bottom: 22px;
  }
  .contact-icon {
    width: 26px;
    height: 26px;
    background: var(--gold);
    border-radius: 4px;
    display: flex;
    align-items: center;
    justify-content: center;
    flex: none;
  }
  .contact-icon svg { width: 15px; height: 15px; }
  .contact-text {
    font-size: 11px;
    line-height: 1.5;
    color: var(--muted);
    letter-spacing: 0.04em;
  }
  .holder {
    position: absolute;
    left: 44px;
    bottom: 44px;
  }
  .holder-name {
    margin: 0;
    font-size: 17px;
    font-weight: 700;
    color: var(--ink);
    letter-spacing: 0.06em;
    text-transform: uppercase;
  }
  .holder-role {
    margin: 4px 0 0;
    font-size: 10px;
    font-weight: 400;
    color: var(--gold);
    letter-spacing: 0.14em;
    text-transform: uppercase;
  }

  .brand {
    position: absolute;
    inset: 0;
    display: flex;
    flex-direction: column;
    align-items: center;
    justify-content: center;
  }
  .brand-name {
    margin: 0;
    font-size: 40px;
    font-weight: 300;
    color: var(--gold);
    letter-spacing: 0.02em;
  }
  .brand-tagline {
    margin: 8px 0 0;
    font-size: 11px;
    font-weight: 400;
    color: var(--gold);
    letter-spacing: 0.3em;
    text-transform: uppercase;
  }
</style>
</head>
<body>
<main class="stage">
  <section class="card card--contact" aria-label="Business card, contact side">
    <ul class="contact-list">
      <li class="contact-item">
        <span class="contact-icon">
          <svg viewBox="0 0 16 16" fill="#fff"><path d="M4 1.5l2.2 3-1.3 1.6c.8 1.8 2.2 3.2 4 4l1.6-1.3 3 2.2-1.2 2.5C7 13.3 2.7 9 1.5 3z"/></svg>
        </span>
        <span class="contact-text">010 482 3391<br>011 527 0846</span>
      </li>
      <li class="contact-item">
        <span class="contact-icon">
          <svg viewBox="0 0 16 16" fill="none" stroke="#fff" stroke-width="1.4"><circle cx="8" cy="8" r="6"/><path d="M2 8h12M8 2c2 2 2 10 0 12M8 2c-2 2-2 10 0 12"/></svg>
        </span>
        <span class="contact-text">kbh@summitquarry.com.eg<br>www.summitquarry.com.eg</span>
      </li>
      <li class="contact-item">
        <span class="contact-icon">
          <svg viewBox="0 0 16 16" fill="#fff"><path d="M8 1a5 5 0 0 1 5 5c0 3.6-5 9-5 9S3 9.6 3 6a5 5 0 0 1 5-5zm0 3a2 2 0 1 0 0 4 2 2 0 0 0 0-4z"/></svg>
        </span>
        <span class="contact-text">14 Shari' Nakhil el Wadi, Rawdatein<br>Giza, 12487, Egypt</span>
      </li>
    </ul>
    <div class="holder">
      <p class="holder-name">Karim Haddouri</p>
      <p class="holder-role">Eng. · C.E.O</p>
    </div>
  </section>

  <section class="card card--brand" aria-label="Business card, brand side">
    <div class="brand">
      <p class="brand-name">Summit Quarry</p>
      <p class="brand-tagline">Marble &amp; Granite</p>
    </div>
  </section>
</main>
</body>
</html>
```